Visitenkarten-Design für Frauenarztpraxis
Zielgruppe
Frauenarztpraxis
Aufgabenstellung
auf der einen Seite Name (Dr. med. Lindner Theresa), auf der anderen Seite Fachärztin für Gynäkologie und Geburtshilfe, Lärchenweg 8, 6112 Wattens, Tel. Nr. 05338/21934, Termine nach Vereinbarung

```html
<!DOCTYPE html>
<html lang="de">
<head>
<meta charset="utf-8">
<title>Visitenkarte – Dr. med. Theresa Lindner</title>
<link rel="stylesheet" href="https://fonts.googleapis.com/css2?family=Ubuntu:ital,wght@0,300;0,400;0,500;1,400&display=swap">
<style>
  :root {
    --page: #ffffff;
    --purple: #4e237e;
    --lilac: #c9a6d1;
    --lilac-soft: #d9c3e3;
    --lilac-pale: #ece3f0;
    --ink: #222222;
    --grey: #9a9a9a;
    --tel: #c596cf;
    --card-shadow: 0 6px 18px rgba(0,0,0,0.22);
  }
  * { margin: 0; padding: 0; box-sizing: border-box; }
  html, body { width: 1000px; height: 1200px; overflow: hidden; }
  body {
    background: var(--page);
    font-family: "Ubuntu", sans-serif;
    position: relative;
  }
  .card {
    position: absolute;
    left: 100px;
    width: 800px;
    height: 516px;
    box-shadow: var(--card-shadow);
    overflow: hidden;
  }
  .card--front { top: 50px; background: var(--purple); }
  .card--back { top: 634px; background: #ffffff; }

  .brand-mark {
    position: absolute;
    left: 64px; top: 180px;
    width: 168px; height: 168px;
  }
  .front-name {
    position: absolute;
    left: 104px; top: 328px;
    color: var(--lilac);
    white-space: nowrap;
  }
  .front-name .title { font-size: 27px; font-weight: 300; color: var(--lilac-soft); }
  .front-name .name { font-size: 62px; font-weight: 400; letter-spacing: 1px; }
  .front-specialty {
    position: absolute;
    left: 104px; top: 410px;
    font-size: 22px; font-weight: 300;
    color: var(--lilac-soft);
  }

  .back-name {
    position: absolute;
    left: 76px; top: 90px;
    white-space: nowrap;
  }
  .back-name .title { font-size: 27px; font-weight: 300; color: var(--ink); }
  .back-name .name { font-size: 42px; font-weight: 500; color: var(--purple); }
  .back-specialty {
    position: absolute;
    left: 76px; top: 142px;
    font-size: 21px; font-weight: 300;
    color: var(--grey);
  }
  .contact {
    position: absolute;
    left: 76px; top: 250px;
    font-size: 27px; font-weight: 300;
    color: var(--ink);
    line-height: 38px;
  }
  .contact .sep, .contact .label { color: var(--tel); }
  .appointments {
    position: absolute;
    left: 78px; top: 390px;
    font-size: 27px; font-style: italic; font-weight: 400;
    color: var(--purple);
  }
  .brand-mark--faint {
    position: absolute;
    left: 495px; top: 192px;
    width: 265px; height: 265px;
  }
</style>
</head>
<body>
  <section class="card card--front" aria-label="Vorderseite">
    <svg class="brand-mark" viewBox="0 0 100 100" role="img" aria-label="Praxiszeichen">
      <circle cx="50" cy="50" r="48" fill="var(--lilac)"/>
    </svg>
    <div class="front-name"><span class="title">Dr. med.</span> <span class="name">Theresa Lindner</span></div>
    <p class="front-specialty">Fachärztin für Gynäkologie und Geburtshilfe</p>
  </section>

  <section class="card card--back" aria-label="Rückseite">
    <div class="back-name"><span class="title">Dr. med.</span> <span class="name">Theresa Lindner</span></div>
    <p class="back-specialty">Fachärztin für Gynäkologie und Geburtshilfe</p>
    <p class="contact">
      Lärchenweg 8 <span class="sep">|</span> 6178 Almdorf<br>
      <span class="label">Tel.:</span>&nbsp; 05338 / 21 93 4
    </p>
    <p class="appointments">Termine nach Vereinbarung</p>
    <svg class="brand-mark--faint" viewBox="0 0 100 100" role="img" aria-label="Dezentes Praxiszeichen als Hintergrund">
      <circle cx="50" cy="50" r="48" fill="var(--lilac-pale)"/>
    </svg>
  </section>
</body>
</html>
```